New Wordpress Website

We need a new wordpress website for our IT Association. Our main corporate colour is orange. Style Guideline attached.
The association is an NFP for IT Professionals. An opportunity for our members to collaborate and grow as a community.

Current website can be found at: www.crestlanetechguild.org

Target Market(s)

IT Professionals and Small Business Owners who need IT Information

Industry/Entity Type

Information Technology

Coding

Coded - Design and coding required

Colors
f37122

```html
<!DOCTYPE html>
<html lang="en">
<head>
<meta charset="utf-8">
<title>Crestlane Tech Guild</title>
<link href="https://fonts.googleapis.com/css2?family=Archivo:wght@400;700&family=Oswald:wght@300&display=swap" rel="stylesheet">
<style>
:root{
  --orange:#f37122;
  --orange-soft:#f7c4a4;
  --grey-text:#5f5f5f;
  --body-text:#555;
  --light:#ececec;
  --white:#fff;
}
*{box-sizing:border-box;margin:0;padding:0}
html,body{width:1200px;height:3122px;overflow:hidden}
body{position:relative;font-family:'Archivo',sans-serif;color:var(--body-text);background:var(--white)}
.abs{position:absolute}
.hero{left:0;top:0;width:1200px;height:674px;background:linear-gradient(100deg,#dcdcdc 0%,#c9c9c9 60%,#b8b8b8 100%)}
.hero-figure{left:360px;top:120px;width:640px;height:540px;background:radial-gradient(ellipse at 60% 70%,#f07a2a 0%,#e98c4c 30%,rgba(200,200,200,0) 65%)}
.logo{left:82px;top:52px;display:flex;align-items:center;gap:10px}
.logo-mark{width:40px;height:40px;border-radius:50%;border:4px solid var(--orange)}
.logo-name{font-weight:700;font-size:21px;color:#333;line-height:1}
.logo-sub{font-size:11px;color:#333;letter-spacing:.5px}
.search{left:904px;top:15px;width:213px;height:29px;border:1px solid #888;background:#e6e6e6}
.nav{left:447px;top:60px;display:flex;gap:30px;font-family:'Oswald',sans-serif;font-weight:300;font-size:20px;color:#444}
.nav .active{color:var(--orange)}
.nav .drop{position:relative}
.nav .drop::after{content:"";position:absolute;left:50%;top:28px;width:6px;height:6px;border-right:2px solid var(--orange);border-bottom:2px solid var(--orange);transform:translateX(-50%) rotate(45deg)}
.hero-title{left:85px;top:182px;font-size:86px;line-height:97px;color:var(--orange);font-weight:400}
.btn{display:flex;align-items:center;justify-content:center;border-radius:22px;font-weight:700;font-size:11px}
.btn-fill{background:var(--orange);color:var(--white)}
.btn-line{border:2px solid var(--orange);color:var(--orange)}
.intro-title{left:83px;top:715px;font-size:37px;line-height:50px;font-weight:700;color:var(--grey-text);width:600px}
.hl{color:var(--orange)}
.intro-text{left:83px;top:825px;width:565px;font-size:18px;line-height:31.5px}
.intro-text p+p{margin-top:9px}
.video{left:730px;top:725px;width:387px;height:305px;background:linear-gradient(180deg,#e8e8e8 0%,#d8d8d8 55%,#ee8a45 100%)}
.play{left:893px;top:846px;width:64px;height:64px;border:3px solid #fff;border-radius:50%}
.feature{width:260px;text-align:center}
.feature h3{font-size:38px;color:var(--grey-text);margin-top:10px}
.feature p{font-size:18px;line-height:31px;width:200px;margin:0 auto}
.feature-btn{width:94px;height:40px;font-size:11px}
.chapter-title{left:181px;top:1804px;font-size:39px;line-height:50px;font-weight:700;color:var(--grey-text)}
.map{left:602px;top:1691px;width:418px;height:376px;background:linear-gradient(135deg,#f2f2f2,#e4e4e4)}
.section-title{left:0;width:1200px;text-align:center;font-size:38px;font-weight:700;color:var(--orange)}
.partner{top:2256px;font-size:30px;font-weight:700;text-align:center;white-space:nowrap}
.arrow{z-index:2}
.testimonial-photo{left:216px;top:2473px;width:390px;height:375px;background:linear-gradient(180deg,#d9d9d9,#6f6f6f)}
.quote{left:636px;top:2508px;width:360px;font-size:18px;line-height:31px}
.footer{left:0;top:2848px;width:1200px;height:274px;background:var(--orange);color:var(--white);overflow:hidden}
.col{position:absolute;top:60px;width:325px}
.col h2{font-size:38px;font-weight:700;margin-bottom:14px}
.col p{font-size:18px;line-height:31px}
</style>
</head>
<body>

<div class="abs hero" role="img" aria-label="Photo of a smiling man working on a laptop in an orange bean bag chair">
  <div class="abs hero-figure"></div>
</div>

<div class="abs logo">
  <div class="logo-mark"></div>
  <div><div class="logo-name">Crestlane</div><div class="logo-sub">TECH GUILD</div></div>
</div>
<div class="abs search">
  <svg class="abs" style="left:194px;top:8px" width="12" height="12" viewBox="0 0 12 12"><circle cx="5" cy="5" r="3.6" fill="none" stroke="#444" stroke-width="1.2"/><line x1="7.7" y1="7.7" x2="11" y2="11" stroke="#444" stroke-width="1.2"/></svg>
</div>
<nav class="abs nav">
  <span class="active">How It Works</span><span>Join</span><span>Chapters Members</span><span>Partners</span>
  <span class="drop">Media</span><span class="drop">Events</span><span class="drop">Shop</span><span class="drop">About Us</span>
</nav>

<h1 class="abs hero-title">Strength<br>in numbers.</h1>
<div class="abs btn btn-fill" style="left:82px;top:373px;width:257px;height:41px">Join Us</div>
<div class="abs btn btn-line" style="left:82px;top:430px;width:257px;height:41px">Download Brochure</div>

<h2 class="abs intro-title">Grow your <span class="hl">business,</span> Grow your <span class="hl">reputation.</span></h2>
<div class="abs intro-text">
  <p><span class="hl">Crestlane</span> Tech Guild is Australia’s leading industry association for IT business owners and professionals specialising in IT solutions for small and medium business.</p>
  <p>As a <span class="hl">Crestlane</span> Tech Guild member you can draw upon, and add to, the collective knowledge bank of best-practice solutions and expert opinions garnered from a national network of IT business owners and professionals..</p>
</div>
<div class="abs video" role="img" aria-label="Video still of a smiling woman in an orange top"></div>
<div class="abs play"><svg class="abs" style="left:22px;top:19px" width="20" height="20" viewBox="0 0 20 20"><path d="M4 2 L17 10 L4 18Z" fill="#fff"/></svg></div>

<div class="abs feature" style="left:116px;top:1155px">
  <svg width="120" height="122" viewBox="0 0 120 122" fill="none" stroke="#f37122" stroke-width="5"><rect x="16" y="5" width="96" height="112" rx="8"/><line x1="30" y1="5" x2="30" y2="117"/><line x1="6" y1="30" x2="22" y2="30"/><line x1="6" y1="60" x2="22" y2="60"/><line x1="6" y1="90" x2="22" y2="90"/><circle cx="71" cy="40" r="12"/><path d="M50 80 Q71 50 92 80 Z"/><line x1="50" y1="96" x2="92" y2="96"/></svg>
  <h3>Seek.</h3>
  <p>Liberate your time and find proven IT solutions fast via the Crestlane Tech Guild Forum.</p>
</div>
<div class="abs feature" style="left:470px;top:1155px">
  <svg width="120" height="122" viewBox="0 0 120 122" fill="none" stroke="#f37122" stroke-width="5"><circle cx="28" cy="18" r="10"/><path d="M14 40 h28 v75 h-28z"/><path d="M52 70 h28 v45 h-28z"/><circle cx="95" cy="55" r="16"/><path d="M90 50 q5 -8 10 0 q0 4 -5 7 v3"/><path d="M70 10 h22 v20 h-22z"/></svg>
  <h3>Solve.</h3>
  <p>Create a more efficient and effective business, and deliver greater value to your customers via fast, effective problem-solving.</p>
</div>
<div class="abs feature" style="left:824px;top:1140px">
  <svg width="130" height="137" viewBox="0 0 130 137" fill="none" stroke="#f37122" stroke-width="5"><circle cx="60" cy="30" r="11"/><path d="M42 62 q18 -26 36 0z"/><circle cx="22" cy="92" r="10"/><path d="M6 132 v-14 h32 v14z"/><circle cx="102" cy="92" r="10"/><path d="M86 132 v-14 h32 v14z"/><path d="M28 70 q6 -24 24 -30"/><path d="M80 38 q20 10 22 34"/><path d="M48 120 h30"/><path d="M92 5 l20 20 l-12 12"/></svg>
  <h3>Share.</h3>
  <p>Join the collective buying power and influence of Australia’s largest industry association for small and medium business IT.</p>
</div>
<div class="abs btn btn-fill feature-btn" style="left:199px;top:1559px">Read More</div>
<div class="abs btn btn-fill feature-btn" style="left:553px;top:1559px">Read More</div>
<div class="abs btn btn-fill feature-btn" style="left:907px;top:1559px">Read More</div>

<h2 class="abs chapter-title">Find your local<br><span class="hl">Crestlane</span> Tech Guild<br>Chapter.</h2>
<div class="abs btn btn-fill" style="left:180px;top:1966px;width:94px;height:38px">Find More</div>
<div class="abs map" role="img" aria-label="Illustration of a folded map with orange location pins"></div>

<h2 class="abs section-title" style="top:2155px">Partners</h2>
<svg class="abs arrow" style="left:84px;top:2243px" width="36" height="68" viewBox="0 0 36 68"><path d="M34 2 L2 34 L34 66" fill="none" stroke="#555" stroke-width="2"/></svg>
<svg class="abs arrow" style="left:1052px;top:2243px" width="36" height="68" viewBox="0 0 36 68"><path d="M2 2 L34 34 L2 66" fill="none" stroke="#555" stroke-width="2"/></svg>
<div class="abs partner" style="left:150px;width:170px;color:#2f7fc1">Northbyte</div>
<div class="abs partner" style="left:340px;width:200px;color:var(--orange)">QuickForge</div>
<div class="abs partner" style="left:590px;width:210px;color:#1f2a44">CoreLatch</div>
<div class="abs partner" style="left:828px;width:200px;color:#1f4fa0">Shieldmere</div>

<h2 class="abs section-title" style="top:2400px">Testimonials</h2>
<div class="abs testimonial-photo" role="img" aria-label="Photo of a businessman in a grey suit holding a tablet"></div>
<svg class="abs arrow" style="left:186px;top:2628px" width="36" height="68" viewBox="0 0 36 68"><path d="M34 2 L2 34 L34 66" fill="none" stroke="#555" stroke-width="2"/></svg>
<svg class="abs arrow" style="left:980px;top:2628px" width="36" height="68" viewBox="0 0 36 68"><path d="M2 2 L34 34 L2 66" fill="none" stroke="#555" stroke-width="2"/></svg>
<p class="abs quote">Our business has grown thanks to Crestlane Tech Guild and has connected us to new business opportunities, created additional revenue and we have completed successful mergers and acquisitions with three other Crestlane Tech Guild Members.</p>

<footer class="abs footer">
  <div class="col" style="left:87px"><h2>Join us.</h2><p>Imagine growing your business to employ 260+ IT business owners and professionals; all with expertise in solutions for small and medium business. When you join Crestlane</p></div>
  <div class="col" style="left:487px"><h2>About us.</h2><p>Crestlane Tech Guild is a not-for profit and was founded in 2011. Uniquely positioned as a conduit for individual IT business owners, professionals, IT service providers and IT vendors to</p></div>
  <div class="col" style="left:887px"><h2>Follow us.</h2></div>
</footer>

</body>
</html>
```